Website Wordpress Design

Hello all,

Real Estate Investor seeking a sleek user friendly word-press website. We are using this site to promote our real estate deals and raising capital from individuals who want to learn how to make money in real estate. The site will have 5 pages, Below you will see files explaining the site format and logo design. The website address is quillstonereserve.com.***Must be able to retrieve word-press log-in username and password for future updates***

Here are some sites we like: feltmoorcapitalhub.com and harborlanecarebuilders.com

Target Market(s)

Individuals 40 and above.

Industry/Entity Type

Real Estate

Contact Information for Business Card

I'm seeking a killer business card design see details below.
Rosa Kimbrel
Managing Partner
TWR Ventures, LLC
418 Garnet Street Suite 362
Brooklyn, NY 11217
Direct:917-304-7821
www.quillstonereserve.com
rosa@qsreserve.com

Number of Pages Required

5+ page

Font styles to use
Serif
Sans Serif

Requirements
Must have
• Good Color schemes and appealing to the eye.
Should not have
• Money symbols or images of houses

```html
<!DOCTYPE html>
<html lang="en">
<head>
<meta charset="utf-8">
<title>Quillstone Reserve</title>
<link rel="stylesheet" href="https://fonts.googleapis.com/css2?family=Questrial&family=Open+Sans:wght@400;600;700&display=swap">
<style>
:root{
  --gold:#b39a66;
  --gold-dark:#a4895a;
  --ink:#1a1a1a;
  --text:#333;
  --muted:#666;
  --dark:#232323;
  --darker:#181818;
  --light:#f2f2f2;
  --white:#fff;
}
*{margin:0;padding:0;box-sizing:border-box}
html,body{width:1200px;height:3077px;overflow:hidden}
body{position:relative;background:var(--white);font-family:"Open Sans",sans-serif;color:var(--text)}
.abs{position:absolute}
.display{font-family:"Questrial",sans-serif}

/* top bar */
.topbar{left:0;top:0;width:1200px;height:33px;background:var(--gold);color:var(--white);font-size:12px;font-weight:600}
.topbar .welcome{left:215px;top:8px}
.topbar .social{right:40px;top:9px;font-size:10px;letter-spacing:.5px;display:flex;gap:12px}

/* header */
.brand{left:55px;top:0;width:173px;height:200px;background:var(--white);z-index:3;border:1px solid #ddd;border-top:none;display:flex;flex-direction:column;align-items:center;justify-content:center;gap:12px}
.brand .dot{width:64px;height:64px;border-radius:50%;background:var(--ink)}
.brand .name{font-family:"Questrial",sans-serif;color:var(--gold);font-size:21px;text-align:center;line-height:1.15;letter-spacing:1px}
.info{top:74px;display:flex;gap:12px;align-items:flex-start;font-size:13px;color:var(--text)}
.info strong{display:block;font-size:15px;color:var(--ink);font-weight:700}
.info.call{left:672px}
.info.hours{left:873px}

/* nav */
.nav{left:0;top:160px;width:1200px;height:41px;background:var(--ink)}
.nav ul{list-style:none;position:absolute;right:58px;top:0;display:flex;gap:31px}
.nav li{color:var(--white);font-size:15px;font-weight:600;line-height:41px;position:relative}
.nav li.active::after{content:"";position:absolute;left:0;right:0;bottom:4px;height:3px;background:var(--gold)}

/* hero */
.hero{left:0;top:201px;width:1200px;height:558px;background:linear-gradient(100deg,#5f6770 0%,#a9b3bb 30%,#d8e4ea 55%,#c4dde5 80%,#b6d5de 100%)}
.enquiry{left:800px;top:308px;width:338px;height:359px;background:var(--white);box-shadow:0 2px 8px rgba(0,0,0,.15)}
.enquiry h3{background:var(--gold);color:var(--white);font-family:"Questrial",sans-serif;font-weight:400;font-size:25px;height:55px;line-height:55px;padding-left:15px}
.enquiry p{font-size:13px;text-align:center;padding:12px 30px 0;color:var(--muted);line-height:1.45}
.field{display:block;margin:0 auto;width:285px;background:#f4f4f4;border:1px solid #e6e6e6;font-size:12px;color:#999;padding:10px 12px}
.field.name{margin-top:22px;height:39px}
.field.email{margin-top:8px;height:39px}
.field.msg{margin-top:8px;height:70px}
.enquiry .submit{display:block;margin:12px auto 0;width:122px;height:42px;background:var(--ink);color:var(--white);font-weight:700;font-size:19px;text-align:center;line-height:42px}

/* section headings */
.heading{font-family:"Questrial",sans-serif;font-size:39px;color:var(--ink);text-transform:uppercase}
.heading .accent{color:var(--gold)}
.heading-rule{height:3px;background:var(--gold)}
.about-title{left:0;width:1200px;top:822px;text-align:center}
.about-rule{left:368px;top:872px;width:300px}
.about-copy{left:230px;top:895px;width:780px;text-align:center;font-size:13px;line-height:25px;color:var(--text)}

/* feature cards */
.feature{top:1021px;width:313px;height:281px;background:var(--gold);padding:5px}
.feature .photo{width:303px;height:225px}
.feature .label{color:var(--white);font-family:"Questrial",sans-serif;font-size:26px;text-align:center;line-height:50px}

/* services */
.services{left:0;top:1405px;width:1200px;height:550px;background:linear-gradient(180deg,#2a2a2a,#1c1c1c 60%,#252525)}
.services .title{left:0;width:1200px;top:62px;text-align:center;color:var(--white);font-family:"Questrial",sans-serif;font-size:46px}
.services .sub{left:0;width:1200px;top:126px;text-align:center;color:var(--gold);font-size:13px}
.service{top:195px;width:220px;text-align:center}
.service .pin{display:block;margin:0 auto}
.service h4{font-family:"Questrial",sans-serif;font-weight:400;color:var(--gold);font-size:27px;margin-top:24px}
.service p{color:#e4e4e4;font-size:12px;line-height:21px;margin-top:14px;padding:0 8px}

/* blog */
.blog-title{left:137px;top:2042px}
.blog-rule{left:137px;top:2090px;width:236px}
.arrow{top:2047px;width:36px;height:36px}
.post{top:2178px;width:313px;height:447px;background:var(--light)}
.post .photo{width:313px;height:252px}
.post h5{font-family:"Questrial",sans-serif;font-weight:400;font-size:23px;color:var(--ink);margin:30px 0 0 12px}
.post p{font-size:12px;line-height:19px;color:var(--muted);margin:12px 14px 0 12px}
.post .more{display:inline-block;margin:20px 0 0 12px;width:101px;height:35px;line-height:35px;text-align:center;background:var(--gold);color:var(--white);font-size:14px;font-weight:600}

/* footer */
.footer{left:0;top:2728px;width:1200px;height:307px;background:var(--dark);color:#bdbdbd}
.footer h6{position:absolute;color:var(--white);font-size:19px;font-weight:600;top:47px}
.footer .about{left:47px;top:102px;width:340px;font-size:13px;line-height:21px;color:#9a9a9a}
.footer .contact-row{left:47px;font-size:13px;display:flex;align-items:center;gap:10px;color:#bdbdbd}
.footer .links{top:102px;list-style:none;font-size:12px;color:#d6d6d6}
.footer .links li{height:33px}
.subscribe-input{left:820px;top:115px;width:277px;height:38px;background:var(--white)}
.subscribe-btn{left:1097px;top:115px;width:56px;height:38px;background:var(--gold)}
.footer .note{left:820px;top:165px;font-size:13px;color:#9a9a9a}
.footer .divider{left:820px;top:200px;width:333px;height:1px;background:#3a3a3a}
.footer .soc{font-size:12px;color:#d6d6d6;display:flex;align-items:center;gap:10px}
.footer .soc i{display:inline-block;width:7px;height:7px;background:#d6d6d6}
.copyright{left:0;top:3035px;width:1200px;height:42px;background:var(--darker);color:#cfcfcf;font-size:12px;text-align:center;line-height:42px}
</style>
</head>
<body>

<div class="abs topbar">
  <span class="abs welcome">Welcome to Quillstone Reserve</span>
  <span class="abs social"><span>Chatterleaf</span><span>Chirpline</span><span>Linkhall</span></span>
</div>

<div class="abs brand">
  <span class="dot"></span>
  <span class="name">QUILLSTONE<br>RESERVE</span>
</div>

<div class="abs info call">
  <svg width="14" height="26" viewBox="0 0 14 26"><path d="M10 2 C3 4 2 12 4 18 C5 22 8 24 11 23 L12 19 L9 17 L7 19 C6 16 6 10 7 8 L10 9 L11 5 Z" fill="#b39a66"/></svg>
  <div><strong>Call us on</strong>+614 220 7815, 4471029</div>
</div>
<div class="abs info hours">
  <svg width="24" height="24" viewBox="0 0 24 24"><circle cx="12" cy="12" r="10" fill="none" stroke="#b39a66" stroke-width="2"/><path d="M12 6v6l4 3" fill="none" stroke="#b39a66" stroke-width="2"/></svg>
  <div><strong>Opening Houres</strong>Monday to friday | 8:30am to 5:30pm</div>
</div>

<nav class="abs nav">
  <ul>
    <li class="active">HOME</li><li>OUR FIRM</li><li>PRACTICE</li><li>AREAS</li><li>ATTORNEYS</li><li>BLOG</li><li>SHOP</li><li>CONTACT US</li>
  </ul>
</nav>

<div class="abs hero" role="img" aria-label="Photo of a business meeting with a signed contract on a desk"></div>

<form class="abs enquiry">
  <h3>Consultaion or Enquiry us</h3>
  <p>As I have been traveling more and working with assisted living providers</p>
  <span class="field name">Name</span>
  <span class="field email">Email</span>
  <span class="field msg">Message</span>
  <span class="submit">Submit</span>
</form>

<h2 class="abs heading about-title">About <span class="accent">Quillstone Reserve</span></h2>
<div class="abs heading-rule about-rule"></div>
<p class="abs about-copy">As I have been traveling more and working with assisted living providers all over the country, one thing has become completely clear As I have been traveling more and working with assisted living providers all over the country, one thing has become completely clear</p>

<div class="abs feature" style="left:62px">
  <div class="photo" role="img" aria-label="Photo of colleagues reviewing a tablet at a desk" style="background:linear-gradient(135deg,#3d3a36,#7a6c5c)"></div>
  <div class="label">Hire Us</div>
</div>
<div class="abs feature" style="left:443px">
  <div class="photo" role="img" aria-label="Photo of a team planning a project together" style="background:linear-gradient(135deg,#e6e2da,#b8a48a)"></div>
  <div class="label">Work with our Team</div>
</div>
<div class="abs feature" style="left:822px">
  <div class="photo" role="img" aria-label="Photo of a sign being handed over outdoors" style="background:linear-gradient(180deg,#6f9fd3,#cbd9e4 60%,#8f8a6c)"></div>
  <div class="label">Succeed!</div>
</div>

<section class="abs services" role="region" aria-label="Services">
  <h2 class="abs title">WE PROVIDE SERVICES</h2>
  <p class="abs sub">As I have been traveling more and working with assisted living</p>

  <div class="abs service" style="left:17px">
    <svg class="pin" width="128" height="138" viewBox="0 0 128 138"><path d="M64 136 L50 120 A60 60 0 1 1 78 120 Z" fill="none" stroke="#fff" stroke-width="3"/><path d="M42 48v32h44M52 76V62M62 76V54M72 76V58" fill="none" stroke="#fff" stroke-width="4"/></svg>
    <h4>Marketing</h4>
    <p>I recently parted ways with a facility/their ownership as the management company. We had done our job, and we had done</p>
  </div>
  <div class="abs service" style="left:249px">
    <svg class="pin" width="128" height="138" viewBox="0 0 128 138"><path d="M64 136 L50 120 A60 60 0 1 1 78 120 Z" fill="none" stroke="#fff" stroke-width="3"/><rect x="38" y="40" width="52" height="36" rx="2" fill="none" stroke="#fff" stroke-width="4"/><path d="M56 86h16M64 76v10" stroke="#fff" stroke-width="4"/><circle cx="58" cy="58" r="8" fill="#fff"/></svg>
    <h4>Feasibility</h4>
    <p>I recently parted ways with a facility/their ownership as the management company. We had done our job, and we had done</p>
  </div>
  <div class="abs service" style="left:470px">
    <svg class="pin" width="128" height="138" viewBox="0 0 128 138"><path d="M64 136 L50 120 A60 60 0 1 1 78 120 Z" fill="#b39a66"/><rect x="46" y="36" width="36" height="48" rx="3" fill="none" stroke="#fff" stroke-width="3"/><path d="M54 48h20M54 56h20M54 64h20M54 72h14" stroke="#fff" stroke-width="3"/></svg>
    <h4>Training</h4>
    <p>I recently parted ways with a facility/their ownership as the management company. We had done our job, and we had done</p>
  </div>
  <div class="abs service" style="left:710px">
    <svg class="pin" width="128" height="138" viewBox="0 0 128 138"><path d="M64 136 L50 120 A60 60 0 1 1 78 120 Z" fill="none" stroke="#fff" stroke-width="3"/><circle cx="50" cy="50" r="8" fill="#fff"/><path d="M36 78a14 14 0 0 1 28 0Z" fill="#fff"/><path d="M70 50h20M70 60h20M70 70h20" stroke="#fff" stroke-width="4"/></svg>
    <h4>Consulting</h4>
    <p>I recently parted ways with a facility/their ownership as the management company. We had done our job, and we had done</p>
  </div>
  <div class="abs service" style="left:926px">
    <svg class="pin" width="128" height="138" viewBox="0 0 128 138"><path d="M64 136 L50 120 A60 60 0 1 1 78 120 Z" fill="none" stroke="#fff" stroke-width="3"/><circle cx="64" cy="60" r="22" fill="none" stroke="#fff" stroke-width="3"/><circle cx="64" cy="60" r="6" fill="#fff"/><circle cx="64" cy="38" r="4" fill="#fff"/><circle cx="86" cy="60" r="4" fill="#fff"/><circle cx="64" cy="82" r="4" fill="#fff"/><circle cx="42" cy="60" r="4" fill="#fff"/></svg>
    <h4>Development</h4>
    <p>I recently parted ways with a facility/their ownership as the management company. We had done our job, and we had done</p>
  </div>
</section>

<h2 class="abs heading blog-title">From Our Blog</h2>
<div class="abs heading-rule blog-rule"></div>
<svg class="abs arrow" style="left:1059px" viewBox="0 0 36 36"><circle cx="18" cy="18" r="16" fill="none" stroke="#222" stroke-width="2"/><path d="M21 11l-7 7 7 7" fill="none" stroke="#222" stroke-width="2.5"/></svg>
<svg class="abs arrow" style="left:1100px" viewBox="0 0 36 36"><circle cx="18" cy="18" r="16" fill="none" stroke="#222" stroke-width="2"/><path d="M15 11l7 7-7 7" fill="none" stroke="#222" stroke-width="2.5"/></svg>

<article class="abs post" style="left:62px">
  <div class="photo" role="img" aria-label="Photo of high-rise apartment towers" style="background:linear-gradient(180deg,#9cc3e4,#c9a98e 60%,#8a8a7c)"></div>
  <h5>Open New? Or buy existing?</h5>
  <p>One of the biggest questions that I receive from people who want to get started in assisted living is, "Do we open...</p>
  <span class="more">Read More</span>
</article>
<article class="abs post" style="left:443px">
  <div class="photo" role="img" aria-label="Photo illustrating a property investment" style="background:linear-gradient(180deg,#f4f1ec,#a8825e 55%,#8c9a7a)"></div>
  <h5>Open New? Or buy existing?</h5>
  <p>One of the biggest questions that I receive from people who want to get started in assisted living is, "Do we open...</p>
  <span class="more">Read More</span>
</article>
<article class="abs post" style="left:822px">
  <div class="photo" role="img" aria-label="Photo illustrating savings for property" style="background:linear-gradient(180deg,#eef0f2,#c6b79a 60%,#a08755)"></div>
  <h5>Open New? Or buy existing?</h5>
  <p>One of the biggest questions that I receive from people who want to get started in assisted living is, "Do we open...</p>
  <span class="more">Read More</span>
</article>

<footer class="abs footer">
  <h6 style="left:47px">Contact Us</h6>
  <p class="abs about">Ledgerline Advisory is one of the world's Leading financial consulting firms.</p>
  <div class="abs contact-row" style="top:162px"><svg width="10" height="14" viewBox="0 0 10 14"><path d="M5 0a5 5 0 0 1 5 5c0 4-5 9-5 9S0 9 0 5a5 5 0 0 1 5-5z" fill="#bdbdbd"/><circle cx="5" cy="5" r="2" fill="#232323"/></svg>27 Marlow Quay, Brennock, Westford, R93 KX41</div>
  <div class="abs contact-row" style="top:195px"><svg width="12" height="12" viewBox="0 0 12 12"><path d="M2 0l3 3-2 2c1 2 2 3 4 4l2-2 3 3-2 2C5 12 0 7 0 2z" fill="#bdbdbd"/></svg>00353-86-2207193</div>
  <div class="abs contact-row" style="top:228px"><svg width="13" height="10" viewBox="0 0 13 10"><rect width="13" height="10" fill="#bdbdbd"/><path d="M0 0l6.5 5L13 0" fill="none" stroke="#232323"/></svg>contact@ledgerlineadv.com</div>
  <div class="abs contact-row" style="top:261px"><svg width="13" height="11" viewBox="0 0 13 11"><rect x=".5" y=".5" width="12" height="8" fill="none" stroke="#bdbdbd"/><path d="M4 10.5h5" stroke="#bdbdbd"/></svg>www.ledgerlineadv.com</div>

  <h6 style="left:480px">Explore</h6>
  <ul class="abs links" style="left:482px;top:105px"><li>Home</li><li>Service</li><li>News</li><li>Bonds</li><li>Investments</li><li>Stocks</li></ul>
  <ul class="abs links" style="left:613px;top:102px"><li>About Us</li><li>Testimonials</li><li>Contact Us</li><li>Commodities</li><li>Retirement</li><li>Trends</li></ul>

  <h6 style="left:820px;top:52px">Subscribe</h6>
  <div class="abs subscribe-input"></div>
  <svg class="abs subscribe-btn" viewBox="0 0 56 38"><rect width="56" height="38" fill="#b39a66"/><rect x="19" y="13" width="18" height="12" fill="#fff"/><path d="M19 13l9 7 9-7" fill="none" stroke="#b39a66" stroke-width="1.5"/></svg>
  <p class="abs note">Get Latest updates and offers.</p>
  <div class="abs divider"></div>
  <span class="abs soc" style="left:820px;top:230px"><i></i>Chatterleaf</span>
  <span class="abs soc" style="left:953px;top:230px"><i></i>Circlepost</span>
  <span class="abs soc" style="left:820px;top:265px"><i></i>Chirpline</span>
  <span class="abs soc" style="left:953px;top:265px"><i></i>Linkhall</span>
</footer>

<div class="abs copyright">© 2016 Quillstone Reserve Right Reserved.</div>

</body>
</html>
```